Design Our Holiday Magic Coupon

Purpose - The purpose of this project is to create a festive, uplifting, and visually engaging physical coupon that will be mailed to our existing community and warm leads.
The intent is twofold: first, to spark delight and connection by offering a tangible, personal touch during the holiday season; and second, to encourage customers to explore and purchase our programs as they prepare for a strong start to 2026. This mailer is designed to re-engage past buyers, inspire current participants, and gently invite new momentum into their practice through a simple, friendly offer.

Project Description + Scope

This project includes the design and production of a printed coupon ( card format) featuring a 20% discount on purchases of $79 or more. The copy should feel warm, clear, and celebratory without urgency or pressure.

The front of the card will include the headline (“Live Your Best 2026”), bold discount information, and the coupon code FESTIVE20. The back will include a short message reinforcing the tone of possibility and ease, plus simple redemption instructions and the expiry date: December 31, 2025. Deliverables include print-ready artwork, color selection aligned with KH brand style.

one side
LIVE YOUR BEST 2026
Enjoy 20% OFF when you buy $79 or more.
Use code: FESTIVE20
Redeem until end of day December 31, 2025.

Back side - Move with clarity.
Heal with intelligence.
Lead with ease.
Thank you for being part of Kinetic Harmony.
Lots of love, Mara and the whole of Team Mara

Target Market(s)

yoga teachers, yoga lovers, mostly over 50 years, women

Font styles to use
Other font styles liked:
• see attached for feel

Colors
0054AA
0677BA
7BADD7
CADEEF
E8F1F8
0094D4
00A9DD
6FCCEA
C7EBF8
E9F6FB
00AB8E
00BBA5
67D7C9
C6EFE9
E9F9F6
EB3D1F
EC4F4E
F09395
F8D3D4
FCEDEE

Requirements
Nice to have
• see attached

```html
<!DOCTYPE html>
<html lang="en">
<head>
<meta charset="utf-8">
<title>Holiday Coupon – Kinetic Harmony</title>
<link rel="stylesheet" href="https://fonts.googleapis.com/css2?family=Abril+Fatface&family=Archivo:wght@800&family=Didact+Gothic&family=Italianno&family=Nunito:wght@800&family=Open+Sans:wght@400;700&display=swap">
<style>
  :root {
    --page-bg: #eef1f5;
    --card-bg: #8bb0d9;
    --card-bg-light: #a3c1e3;
    --sky: #1a9fdb;
    --band: #17a0db;
    --indigo: #2e3192;
    --muted-indigo: #4b5a9a;
    --white: #ffffff;
    --pale: #c7ebf8;
  }
  * { margin: 0; padding: 0; box-sizing: border-box; }
  html, body { width: 1200px; height: 711px; overflow: hidden; }
  body { background: var(--page-bg); position: relative; }

  .card {
    position: absolute;
    top: 155px;
    width: 560px;
    height: 400px;
    background: var(--card-bg);
    overflow: hidden;
    box-shadow: 0 2px 6px rgba(40, 60, 100, 0.18);
  }
  .card--front { left: 25px; }
  .card--back { left: 615px; }

  .card__pattern {
    position: absolute; inset: 0;
    background: radial-gradient(ellipse at 10% 40%, var(--card-bg-light) 0%, var(--card-bg) 55%);
  }

  /* Front */
  .headline-live {
    position: absolute; left: 94px; top: 40px;
    font-family: "Archivo", "Arial Black", sans-serif; font-weight: 800;
    font-size: 150px; line-height: 1; letter-spacing: -3px;
    color: var(--sky);
  }
  .headline-best {
    position: absolute; left: 100px; top: 138px;
    font-family: "Didact Gothic", "Century Gothic", sans-serif;
    font-size: 70px; line-height: 1; letter-spacing: 1px;
    color: var(--indigo);
  }
  .headline-year {
    position: absolute; left: 96px; top: 200px;
    display: flex; align-items: center;
    font-family: "Didact Gothic", "Century Gothic", sans-serif;
    font-size: 118px; line-height: 1; color: var(--white);
  }
  .discount-seal { width: 96px; height: 96px; margin: 8px 6px 0; }
  .redeem-line {
    position: absolute; left: 0; right: 0; bottom: 12px;
    text-align: center;
    font-family: "Open Sans", sans-serif; font-size: 14px;
    color: var(--muted-indigo);
  }
  .redeem-line strong { color: var(--indigo); font-weight: 700; }
  .divider { color: var(--white); margin: 0 3px; }

  /* Back */
  .mantra {
    position: absolute; left: 0; right: 0; top: 30px;
    text-align: center;
    font-family: "Abril Fatface", serif;
    font-size: 45px; line-height: 55px;
    color: var(--indigo);
  }
  .thanks-band {
    position: absolute; left: 0; right: 0; top: 216px; height: 103px;
    background: var(--band);
    text-align: center; color: var(--white);
  }
  .thanks-band__script {
    font-family: "Italianno", cursive;
    font-size: 68px; line-height: 1; padding-top: 10px;
  }
  .thanks-band__line {
    font-family: "Open Sans", sans-serif; font-size: 17px; margin-top: -4px;
  }
  .signoff {
    position: absolute; left: 0; right: 0; top: 356px;
    text-align: center;
    font-family: "Nunito", sans-serif; font-size: 20px;
    color: var(--muted-indigo);
  }
  .signoff__love { color: var(--indigo); font-weight: 800; }
  .signoff__name { color: var(--white); font-weight: 800; }
  .signoff__rest { font-family: "Open Sans", sans-serif; font-size: 19px; }
  .signoff .divider { color: var(--sky); font-family: "Open Sans", sans-serif; margin: 0 6px; }
</style>
</head>
<body>

<section class="card card--front" aria-label="Coupon front">
  <div class="card__pattern" role="img" aria-label="Soft swirl of pale teardrop shapes"></div>
  <div class="headline-live">LIVE</div>
  <div class="headline-best">your Best</div>
  <div class="headline-year">
    <span>2</span>
    <svg class="discount-seal" viewBox="0 0 100 100" role="img" aria-label="Enjoy 20% off when you buy $79 or more">
      <defs>
        <path id="seal-arc" d="M 16 54 A 34 34 0 1 1 84 54"/>
      </defs>
      <circle cx="50" cy="50" r="48" fill="var(--white)" stroke="var(--indigo)" stroke-width="2" stroke-dasharray="2 2"/>
      <circle cx="50" cy="50" r="45" fill="var(--indigo)"/>
      <circle cx="50" cy="50" r="30" fill="var(--pale)"/>
      <circle cx="50" cy="50" r="22" fill="var(--sky)" opacity="0.55"/>
      <text font-family="Open Sans, sans-serif" font-size="8.5" fill="var(--white)">
        <textPath href="#seal-arc" startOffset="50%" text-anchor="middle">when you buy <tspan fill="var(--sky)" font-weight="700">$79</tspan> or more.</textPath>
      </text>
      <text x="50" y="42" text-anchor="middle" font-family="Open Sans, sans-serif" font-size="8" fill="var(--sky)">Enjoy</text>
      <text x="50" y="58" text-anchor="middle" font-family="Open Sans, sans-serif" font-size="16" font-weight="700" fill="var(--indigo)">20%</text>
      <text x="50" y="67" text-anchor="middle" font-family="Open Sans, sans-serif" font-size="7.5" fill="var(--sky)">OFF</text>
    </svg>
    <span>26</span>
  </div>
  <p class="redeem-line">Use code: <strong>FESTIVE20</strong><span class="divider">|</span>Redeem until end of day <strong>December 31, 2025</strong></p>
</section>

<section class="card card--back" aria-label="Coupon back">
  <div class="card__pattern" role="img" aria-label="Soft swirl of pale teardrop shapes"></div>
  <p class="mantra">Move with clarity.<br>Heal with intelligence.<br>Lead with ease.</p>
  <div class="thanks-band">
    <p class="thanks-band__script">Thank you</p>
    <p class="thanks-band__line">for being part of Kinetic Harmony.</p>
  </div>
  <p class="signoff"><span class="signoff__love">Lots of love</span><span class="divider">|</span><span class="signoff__name">Mara</span> <span class="signoff__rest">and the whole of</span> <span class="signoff__name">Team Mara</span></p>
</section>

</body>
</html>
```